Social Media Advert for Office Fruit Delivery in Dubai

We need an attractive design for social media adverts, for delivering assorted fruit boxes to companies. We will be delivering costume package fruit boxes, with great price, and great quality. Our fruit boxes is +4.5 kg and includes apples, bananas, kiwis, some citrus, and some stone fruit depending on seasonality. Our offer prices are AED 45, which is very competitive as we are wholesalers, and growers of some of our fruits. Our goal is to support health initiative set by responsible companies. Our delivery is free for companies who enrol into weekly delivery programs restricted to Dubai only. We suggest deliveries to be once a week, as our fruit is fresh, and great for consumption in a one week window. Considering each employee on average would consume two pieces of fruits a day, our fruit boxes is ideal for 4 employees in one working week. We need a talented designer, to kick start our sales. You can find more details about this project, and about our company on our website www.lunagrove.co follow us on social media @lunagroveuae

Target Market(s)

age 22-50, based in Dubai working individuals in companies with responsibility to care for it's employees and their health.

Font styles to use
Other font styles liked:
• IYC Avant Garde Gothic LT Bold

Colors

Designer to choose colors to be used in the design.

Requirements
Must have
• - Logo
• - offer price and product
Nice to have
• Check out the 'inspire' in attachments to understand what we are looking for

```html
<!DOCTYPE html>
<html lang="en">
<head>
<meta charset="utf-8">
<title>Luna Grove – Farm Fresh On Your Desk</title>
<link href="https://fonts.googleapis.com/css2?family=Jost:wght@500;600;700&family=Kalam:wght@700&display=swap" rel="stylesheet">
<style>
  :root {
    --sand: #dcb486;
    --lemon: #fbf18d;
    --coral: #e97855;
    --orange: #f58220;
    --white: #ffffff;
    --truck: #f2876a;
  }
  html, body { margin: 0; padding: 0; overflow: hidden; background: var(--sand); }
  .flyer {
    position: relative; width: 856px; height: 1200px; overflow: hidden;
    background: var(--sand); font-family: "Jost", sans-serif;
  }
  .abs { position: absolute; margin: 0; }
  .brand-disc {
    left: 291px; top: 25px; width: 272px; height: 272px; border-radius: 50%;
    background: var(--lemon); display: flex; align-items: center; justify-content: center;
  }
  .brand-name {
    color: var(--coral); font-weight: 700; font-size: 44px; line-height: 1;
    text-align: center; letter-spacing: 1px;
  }
  .headline {
    left: 0; width: 856px; text-align: center; font-weight: 700; line-height: 1;
  }
  .headline-top { top: 330px; font-size: 78px; }
  .headline-top .farm { color: var(--lemon); }
  .headline-top .fresh { color: var(--coral); }
  .headline-bottom { top: 408px; font-size: 84px; color: var(--orange); }
  .tagline {
    left: 0; width: 856px; top: 492px; text-align: center;
    font-family: "Kalam", cursive; font-weight: 700; font-size: 44px; color: var(--coral);
  }
  .swoosh { left: 0; top: 560px; }
  .product-title {
    left: 0; width: 856px; top: 680px; text-align: center; color: var(--white);
    font-weight: 700; font-size: 39px; letter-spacing: 1px;
  }
  .product-intro {
    left: 0; width: 856px; top: 724px; text-align: center; color: var(--lemon);
    font-weight: 600; font-size: 21px; line-height: 26px;
  }
  .step-title { color: var(--white); font-weight: 700; font-size: 15.5px; letter-spacing: .3px; }
  .step-text { color: var(--lemon); font-weight: 500; font-size: 12px; line-height: 14px; }
  .step-favorites-title { left: 263px; top: 845px; }
  .step-favorites-text { left: 263px; top: 887px; width: 220px; }
  .step-order-title { left: 531px; top: 845px; }
  .step-order-text { left: 530px; top: 887px; width: 215px; }
  .step-deliver-title { left: 265px; top: 1000px; }
  .step-deliver-text { left: 263px; top: 1043px; width: 200px; }
  .price-badge { left: 29px; top: 854px; }
  .delivery-visual {
    left: 553px; top: 958px; width: 180px; height: 152px;
  }
  .delivery-tag {
    left: 568px; top: 1000px; width: 115px; height: 80px; background: var(--truck);
    color: var(--white); font-weight: 700; font-size: 36px;
    display: flex; align-items: center; justify-content: center;
  }
  .band { left: 0; top: 1090px; }
  .hours-title { left: 12px; top: 1112px; color: var(--white); font-weight: 700; font-size: 43px; line-height: 1; }
  .hours-time { left: 12px; top: 1158px; color: var(--lemon); font-weight: 700; font-size: 23px; line-height: 1; }
  .order-call {
    left: 370px; width: 486px; top: 1127px; text-align: center; color: var(--white);
    font-weight: 700; font-size: 25px; line-height: 1;
  }
  .order-address {
    left: 370px; width: 486px; top: 1158px; text-align: center; color: var(--lemon);
    font-weight: 600; font-size: 12.5px; line-height: 1;
  }
</style>
</head>
<body>
<div class="flyer">
  <div class="abs brand-disc">
    <p class="brand-name">LUNA<br>GROVE</p>
  </div>

  <h1 class="abs headline headline-top"><span class="farm">FARM</span> <span class="fresh">FRESH</span></h1>
  <h1 class="abs headline headline-bottom">ON YOUR DESK</h1>
  <p class="abs tagline">Healthy Staff , Healthy Business</p>

  <svg class="abs swoosh" width="856" height="160" viewBox="0 0 856 160" aria-hidden="true">
    <path d="M0,86 Q380,-90 856,138 L856,128 Q390,-38 0,112 Z" fill="var(--lemon)"/>
    <path d="M0,112 Q390,-38 856,128 L856,140 Q420,-12 0,148 Z" fill="var(--coral)"/>
  </svg>

  <h2 class="abs product-title">ASSORTED BOX OF FRUITS</h2>
  <p class="abs product-intro">We’re&nbsp; Bringing Farm Fresh Fruits right to your office.<br>Create your own custom crate or we’ll hand select the<br>best flavors in one convenient box!</p>

  <svg class="abs price-badge" width="200" height="200" viewBox="-100 -100 200 200" role="img" aria-label="Starting at AED 45 only">
    <polygon transform="scale(.92)" fill="var(--orange)" stroke="var(--orange)" stroke-width="13" stroke-linejoin="round"
      points="95,0 82.1,22 82.3,47.5 60.1,60.1 47.5,82.3 22,82.1 0,95 -22,82.1 -47.5,82.3 -60.1,60.1 -82.3,47.5 -82.1,22 -95,0 -82.1,-22 -82.3,-47.5 -60.1,-60.1 -47.5,-82.3 -22,-82.1 0,-95 22,-82.1 47.5,-82.3 60.1,-60.1 82.3,-47.5 82.1,-22"/>
    <circle r="77" fill="none" stroke="#fbd7b8" stroke-width="2.5"/>
    <path id="badge-arc" d="M-57,0 A57,57 0 0 1 57,0" fill="none"/>
    <text font-family="Jost, sans-serif" font-weight="700" font-size="17" fill="var(--lemon)" letter-spacing="1.5">
      <textPath href="#badge-arc" startOffset="50%" text-anchor="middle">STARTING AT</textPath>
    </text>
    <text y="20" text-anchor="middle" font-family="Jost, sans-serif" font-weight="700" font-size="32" fill="var(--white)">AED 45</text>
    <text y="52" text-anchor="middle" font-family="Jost, sans-serif" font-weight="700" font-size="32" fill="var(--lemon)">ONLY</text>
  </svg>

  <h3 class="abs step-title step-favorites-title">FIND YOUR FAVORITES...</h3>
  <p class="abs step-text step-favorites-text">You can plan a combination of fruits depending on your preferences or you can choose our best selling Assorted Box of Fruits worth AED 40.00 (Net Wt. 4Kg)</p>

  <h3 class="abs step-title step-order-title">PLACE YOUR ORDER...</h3>
  <p class="abs step-text step-order-text">Call us directly at +9714 5550182 or visit our online storefront at: www.lunagrove.co/fruitdelivery</p>

  <h3 class="abs step-title step-deliver-title">WE’LL BRING IT TO YOU!</h3>
  <p class="abs step-text step-deliver-text">Get your fruit package within 30 minutes after you order. FREE Delivery!</p>

  <div class="abs delivery-visual" role="img" aria-label="Illustration of a delivery truck carrying a gift-wrapped parcel" style="background: linear-gradient(180deg, #e9a47c, #f0935c); border-radius: 14px;"></div>
  <div class="abs delivery-tag">FREE</div>

  <svg class="abs band" width="856" height="110" viewBox="0 1090 856 110" aria-hidden="true">
    <path d="M0,1096 L296,1096 Q314,1096 324,1112 L362,1200 L0,1200 Z" fill="var(--coral)"/>
    <path d="M343,1124 Q345,1118 358,1118 L856,1118 L856,1200 L378,1200 Z" fill="var(--orange)"/>
  </svg>

  <p class="abs hours-title">OPEN HOURS</p>
  <p class="abs hours-time">SAT – THU 8 AM – 8 PM</p>
  <p class="abs order-call">CALL FOR ORDER +971 4 5550182</p>
  <p class="abs order-address">Palm Row Market, Warehouse 12 &amp; 13, Dubai, United Arab Emirates</p>
</div>
</body>
</html>
```